Healthy Supplement featuring Moringa products

Need 3 business card options for our reps to order from Cardloom. Our reps will be ordering from Cardloom once we upload them. Attached is our current designs to show what info needs to be on the cards. Our website is www.tkvitality.com
The business cards will be a template for our reps to order from. Most of our reps are Asian & Hispanic. Please look at our website so you can see who we are to get the look and feel what we need.
Target Market(s)
Adults 30 on up. Health oriented people.
Industry/Entity Type
Health And Wellness
Contact Information for Business Card
Name
Title
Phone
Logo
www.tkvitality.com/my/username
Font styles to use
Requirements
Must have
- Please match our website look and colors. A moringa leaf is nice, but am open to something different.
Nice to have
- Healthy looking and warm, not super cold or too modern.
Should not have
- No harsh colors please.

```html
<!DOCTYPE html>
<html lang="en">
<head>
<meta charset="utf-8">
<title>TK Vitality – Business Card</title>
<link rel="stylesheet" href="https://fonts.googleapis.com/css2?family=Cinzel:wght@400;500&family=Lato:wght@400&display=swap">
<style>
  :root {
    --page-bg: #2a2a2a;
    --card-front: #4b4b4b;
    --leaf-green: #7cb342;
    --leaf-green-dark: #5e9b2f;
    --back-green: #6aac3f;
    --back-green-light: #86bf4c;
    --text-light: #ffffff;
    --divider: #d8d8d8;
  }
  * { margin: 0; padding: 0; box-sizing: border-box; }
  html, body {
    width: 1200px; height: 977px; overflow: hidden;
    background: var(--page-bg);
  }
  .canvas { position: relative; width: 1200px; height: 977px; }

  .card {
    position: absolute;
    width: 701px; height: 399px;
    overflow: hidden;
    box-shadow: 0 6px 14px rgba(0,0,0,0.55);
  }

  /* Front */
  .card--front { left: 154px; top: 65px; background: var(--card-front); }
  .front__foliage {
    position: absolute; left: 0; top: 90px; width: 210px; height: 309px;
    background: radial-gradient(ellipse at 40% 60%, rgba(110,140,90,0.28), rgba(110,140,90,0) 70%);
  }
  .front__brand {
    position: absolute; left: 110px; top: 175px; width: 180px;
    font-family: "Cinzel", serif; font-weight: 500; font-size: 27px;
    line-height: 1.1; color: var(--leaf-green); text-align: center;
    letter-spacing: 1px;
  }
  .front__divider {
    position: absolute; left: 331px; top: 138px; width: 2px; height: 124px;
    background: var(--divider);
  }
  .front__details { position: absolute; left: 359px; top: 140px; }
  .front__name {
    font-family: "Cinzel", serif; font-weight: 400; font-size: 26px;
    color: var(--leaf-green); letter-spacing: 1px; line-height: 1.1;
  }
  .front__title {
    font-family: "Lato", sans-serif; font-size: 18px; color: var(--text-light);
    margin-top: 2px;
  }
  .contact { list-style: none; margin-top: 18px; }
  .contact__item {
    display: flex; align-items: center; gap: 14px;
    font-family: "Lato", sans-serif; font-size: 18px; color: var(--text-light);
    height: 27px;
  }
  .contact__item svg { width: 13px; height: 13px; fill: var(--leaf-green); }
  .front__url {
    position: absolute; left: 0; width: 100%; padding-left: 0; top: 339px;
    text-align: center; padding-right: 0;
    font-family: "Lato", sans-serif; font-size: 18px; color: var(--text-light);
  }
  .front__url span { position: relative; left: 0; }

  /* Back */
  .card--back {
    left: 290px; top: 512px;
    background: linear-gradient(115deg, var(--back-green) 0%, var(--back-green-light) 55%, var(--back-green) 100%);
  }
  .back__arcs { position: absolute; inset: 0; }
  .back__brand {
    position: absolute; left: 40px; top: 150px;
    font-family: "Cinzel", serif; font-weight: 500; font-size: 66px;
    color: var(--text-light); letter-spacing: 3px;
  }
</style>
</head>
<body>
<main class="canvas">

  <section class="card card--front">
    <div class="front__foliage" role="img" aria-label="Faint moringa branch decoration"></div>
    <div class="front__brand">TK VITALITY</div>
    <div class="front__divider"></div>
    <div class="front__details">
      <h1 class="front__name">DANIEL REYES</h1>
      <p class="front__title">Founder &amp; CEO</p>
      <ul class="contact">
        <li class="contact__item">
          <svg viewBox="0 0 24 24" aria-hidden="true"><path d="M6.6 10.8c1.4 2.8 3.8 5.1 6.6 6.6l2.2-2.2c.3-.3.7-.4 1-.2 1.1.4 2.3.6 3.6.6.6 0 1 .4 1 1V20c0 .6-.4 1-1 1C10.6 21 3 13.4 3 4c0-.6.4-1 1-1h3.5c.6 0 1 .4 1 1 0 1.3.2 2.5.6 3.6.1.3 0 .7-.2 1L6.6 10.8z"/></svg>
          +0 (000) 000 0000
        </li>
        <li class="contact__item">
          <svg viewBox="0 0 24 24" aria-hidden="true"><path d="M2 5h20v14H2z M2 5l10 7 10-7" /></svg>
          d_reyes@tkvitality.com
        </li>
      </ul>
    </div>
    <p class="front__url"><span>www.tkvitality.com/my/username</span></p>
  </section>

  <section class="card card--back">
    <svg class="back__arcs" viewBox="0 0 701 399" preserveAspectRatio="none" aria-hidden="true">
      <path d="M0 120 Q300 0 701 60 L701 0 L0 0 Z" fill="#ffffff" opacity="0.05"/>
      <path d="M0 330 Q350 200 701 300 L701 399 L0 399 Z" fill="#ffffff" opacity="0.06"/>
      <path d="M420 0 Q560 200 701 260 L701 0 Z" fill="#ffffff" opacity="0.05"/>
    </svg>
    <div class="back__brand">TK VITALITY</div>
  </section>

</main>
</body>
</html>
```